Animal care facility (Pet Grooming, Doggie daycare, Boarding, Pet Boutique)

Hi there! i came across your wonderful work and would love to work with you! I have a clear image in my head that i want for my bussiness card and stationary. I will go ahead and attach pictures of business cards that i have found to give you an idea of what i would like to see.

My color scheme is a gray back ground and white lettering. So for the card i would like it to be a gray and the logo on the front to be white and done like picture #1. I would like the quality of the card to be a thicker more durable look. I would want just my logo and then underneath my name ( Marisa Thornbury and my title Owner similar to picture #1. I also have somone i am working with so his would need to be (Colin Pratt, General Manager)

Also there is certain information that does need to be on the back of the card so I don't know if a white back with gray lettering would help it be easily read or not.

Alderwick Pet Haven & Spa LLC
862 E. Millrace Rd.
507.264.1193 -Phone
507.268.4410-Fax
Info@alderwickpethavenandspa.com-Email

Grooming- Boarding-Daycare-Pet Boutique

$10.00 OFF First Time Grooming Visit

The font for all of this is using (oranienbaum)
next to the phone fax, email I would like the actual small pictures that I have in one of the photos
Updates

Industry/Entity Type

Pet Care

Requirements
Must have
• Please follow the design of picture 7 I would like to change the direction of the card all together now. I would like the image to be up top and the name and title to be laid out the same and also in the same font as the attached picture. Again I would like all of this on the front to be engraved In white foil on gray matte backing and if we could lighten the color of this card up I would appreciate it but be on the darker side.
• On the back side keep the version you made and flip all the information to be laid out vertically just like the front.

```html
<!DOCTYPE html>
<html lang="en">
<head>
<meta charset="utf-8">
<title>Alderwick Pet Haven &amp; Spa — Business Card</title>
<link rel="stylesheet" href="https://fonts.googleapis.com/css2?family=Oranienbaum&display=swap">
<style>
  :root {
    --stage: #000000;
    --card: #1f2123;
    --card-edge: #2a2c2f;
    --foil: #e4d6a6;
    --foil-deep: #b9a874;
    --ink: #f4f4f2;
    --rule: #e9e9e7;
  }
  * { box-sizing: border-box; margin: 0; padding: 0; }
  html, body {
    width: 1189px; height: 1200px; overflow: hidden;
    background: var(--stage);
    font-family: "Oranienbaum", "Times New Roman", serif;
  }
  .card {
    position: absolute;
    top: 145px;
    width: 483px; height: 846px;
    background: radial-gradient(ellipse at 50% 40%, #25272a 0%, var(--card) 70%);
    box-shadow: 0 0 0 1px var(--card-edge);
  }
  .card--front { left: 74px; }
  .card--back { left: 630px; }

  /* Front */
  .crest {
    position: absolute; left: 64px; top: 157px;
    width: 359px; height: 180px;
    border-radius: 90px 90px 12px 12px;
    background: radial-gradient(ellipse at 50% 45%, var(--foil) 0%, var(--foil-deep) 55%, rgba(185,168,116,0.15) 100%);
    opacity: 0.85;
  }
  .brand {
    position: absolute; left: 0; right: 0; top: 362px;
    text-align: center; color: var(--foil);
    letter-spacing: 1px; line-height: 1;
  }
  .brand__main { display: block; font-size: 36px; }
  .brand__sub { display: block; font-size: 25px; margin-top: 24px; }
  .holder {
    position: absolute; left: 0; right: 0; top: 618px;
    text-align: center; color: var(--foil); line-height: 1;
  }
  .holder__name { font-size: 38px; letter-spacing: 1px; }
  .holder__title { font-size: 25px; margin-top: 12px; }

  /* Back */
  .vline {
    position: absolute;
    writing-mode: vertical-rl;
    transform: rotate(180deg);
    color: var(--ink);
    white-space: nowrap;
    line-height: 1;
    display: flex; align-items: center;
  }
  .contact-row {
    left: 127px; top: 83px; height: 682px;
    justify-content: space-between;
    font-size: 18px;
  }
  .contact-row--email {
    left: 170px; top: 193px; height: 429px;
  }
  .contact-item { display: flex; align-items: center; gap: 8px; }
  .icon { width: 16px; height: 16px; fill: var(--ink); transform: rotate(90deg); }
  .divider {
    position: absolute; top: 0; bottom: 0; width: 2px;
    background: var(--rule);
  }
  .divider--one { left: 210px; }
  .divider--two { left: 271px; }
  .services { left: 226px; top: 100px; height: 645px; font-size: 27px; letter-spacing: 0.5px; justify-content: center; }
  .offer { left: 299px; top: 214px; height: 425px; font-size: 18px; justify-content: center; }
</style>
</head>
<body>
  <section class="card card--front">
    <div class="crest" role="img" aria-label="Foil crest emblem with a seated cat and dog flanking a shield with grooming scissors and comb"></div>
    <div class="brand">
      <span class="brand__main">ALDERWICK PET</span>
      <span class="brand__sub">HAVEN &amp; SPA</span>
    </div>
    <div class="holder">
      <p class="holder__name">Marisa Thornbury</p>
      <p class="holder__title">Owner</p>
    </div>
  </section>

  <section class="card card--back">
    <div class="vline contact-row">
      <span class="contact-item">
        <svg class="icon" viewBox="0 0 16 16"><path d="M8 1a5 5 0 0 0-5 5c0 4 5 9 5 9s5-5 5-9a5 5 0 0 0-5-5zm0 7a2 2 0 1 1 0-4 2 2 0 0 1 0 4z"/></svg>
        862 E. Millrace Rd.
      </span>
      <span class="contact-item">
        <svg class="icon" viewBox="0 0 16 16"><path d="M4 2h3l1 3-2 1.5a9 9 0 0 0 3.5 3.5L11 8l3 1v3a2 2 0 0 1-2 2A11 11 0 0 1 2 4a2 2 0 0 1 2-2z"/></svg>
        507.264.1193
      </span>
      <span class="contact-item">
        <svg class="icon" viewBox="0 0 16 16"><path d="M4 1h7v4H4zM2 6h12v6h-2v3H4v-3H2zm3 4v4h6v-4z"/></svg>
        507.268.4410
      </span>
    </div>
    <div class="vline contact-row contact-row--email">
      <span class="contact-item">
        <svg class="icon" viewBox="0 0 16 16"><path d="M1 3h14v10H1zm1.5 1.5v.3L8 9l5.5-4.2v-.3zm0 2.2v4.8h11V6.7L8 11z"/></svg>
        Info@alderwickpethavenandspa.com
      </span>
    </div>
    <div class="divider divider--one"></div>
    <p class="vline services">Grooming | Boarding | Daycare | Pet Boutique</p>
    <div class="divider divider--two"></div>
    <p class="vline offer">$10.00 OFF First Time Grooming Visit</p>
  </section>
</body>
</html>
```